web site update

I want to get a better website for a small high end remodeling and construction company
I currently have a web site but you will find that it is not good.
www.quenbrickhall.com
We are a high end construction / remodeling company that has been in business since 2003. We primarily work in the mid peninsula of the bay area. Most of our clientele are very educated captains of industry. This group is still the target client.
I had my logo designed by Mint Easel a few years ago and I do like it, I like the orange and black or orange a blue. I don’t have a lot of content on hand as far as professional photographs.
Number of pages not sure and are open to: design pages vs full function website
I think what I am after is a web presence that will seal the deal as we are getting high referrals from past clients.
Construction
1 page

```html
<!DOCTYPE html>
<html lang="en">
<head>
<meta charset="utf-8">
<title>Quenbrick Hall — Construction / Remodeling</title>
<link href="https://fonts.googleapis.com/css2?family=Arimo:wght@400;700&family=Open+Sans:wght@400;600;700&display=swap" rel="stylesheet">
<style>
:root{
  --orange:#f26a10;
  --teal:#2a9fbd;
  --ink:#2b2b2b;
  --text:#6d6d6d;
  --light:#f2f2f2;
  --line:#e3e3e3;
  --footer:#2a2a2a;
  --footer-text:#d6d6d6;
  --white:#ffffff;
}
*{box-sizing:border-box;margin:0;padding:0}
html,body{width:1200px;height:2744px;overflow:hidden}
body{position:relative;background:var(--white);font-family:"Open Sans",Arial,sans-serif;color:var(--text)}
.abs{position:absolute}
.heading{font-family:"Arimo",Arial,sans-serif;font-weight:700;color:var(--ink);text-transform:uppercase}
.center{text-align:center}
.read-more{font-family:"Open Sans",Arial,sans-serif;font-weight:700;font-size:13px;color:var(--orange);text-transform:uppercase}

/* header */
.top-bar{left:0;top:0;width:1200px;height:7px;background:var(--orange)}
.header{left:0;top:7px;width:1200px;height:88px;background:var(--white)}
.brand{left:100px;top:26px;display:flex;align-items:center;gap:14px}
.brand-dot{width:52px;height:52px;border-radius:50%;background:var(--orange)}
.brand-name{font-family:"Arimo",Arial,sans-serif;font-weight:700;font-size:22px;color:var(--ink);letter-spacing:.5px;line-height:1}
.brand-tag{font-family:"Arimo",Arial,sans-serif;font-size:13px;color:var(--ink);letter-spacing:1.5px;margin-top:4px}
.phone-tab{left:883px;top:0;width:214px;height:40px;background:var(--orange);border-radius:0 0 20px 20px;color:var(--white);font-family:"Arimo",Arial,sans-serif;font-weight:700;font-size:20px;display:flex;align-items:center;justify-content:center;gap:10px}
.nav{top:62px;right:100px;display:flex;gap:36px;font-family:"Arimo",Arial,sans-serif;font-weight:700;font-size:14px;color:var(--ink)}
.nav .active{color:var(--orange)}

/* hero */
.hero{left:0;top:95px;width:1200px;height:454px;background:linear-gradient(180deg,#6f7f95 0%,#8d8f86 45%,#6f7d52 80%,#4f6a2c 100%)}
.hero-title{left:0;top:228px;width:1200px;font-size:44px;color:var(--white);text-shadow:0 2px 4px rgba(0,0,0,.35)}
.hero-sub{left:220px;top:282px;width:760px;font-family:"Arimo",Arial,sans-serif;font-weight:700;font-size:18px;line-height:27px;color:var(--white)}
.hero-btn{left:483px;top:358px;width:234px;height:46px;background:var(--orange);color:var(--white);font-family:"Arimo",Arial,sans-serif;font-weight:700;font-size:15px;display:flex;align-items:center;justify-content:center}
.dots{left:567px;top:490px;display:flex;gap:10px}
.dots span{width:26px;height:6px;border-radius:3px;background:rgba(255,255,255,.7)}
.dots span:first-child{background:var(--orange)}

/* welcome */
.section-title{left:0;width:1200px;font-size:27px}
.welcome-text{left:180px;top:642px;width:840px;font-size:12.5px;line-height:23px}
.feature{top:718px;width:300px;text-align:center}
.feature-icon{width:136px;height:136px;border-radius:50%;margin:0 auto;display:flex;align-items:center;justify-content:center}
.feature-icon .ring{width:120px;height:120px;border-radius:50%;border:3px solid rgba(255,255,255,.85)}
.feature h3{font-family:"Arimo",Arial,sans-serif;font-weight:700;font-size:19px;color:var(--ink);margin-top:22px}
.feature p{font-size:13px;line-height:25px;margin-top:6px}
.feature .read-more{display:block;margin-top:10px}

/* projects */
.band{left:0;width:1200px;background:var(--light)}
.arrow-btn{width:39px;height:55px;background:var(--white);border:1px solid var(--line)}
.project{top:1140px;width:237px}
.photo{border:4px solid var(--white);box-shadow:0 0 0 1px var(--line)}
.project h4{font-family:"Arimo",Arial,sans-serif;font-weight:700;font-size:14.5px;color:var(--ink);margin-top:18px;white-space:nowrap}
.project p{font-size:12px;line-height:21px;margin-top:6px}
.project .read-more{display:block;margin-top:10px}

/* why + news */
.why-text{left:100px;top:1786px;width:372px;font-size:12.5px;line-height:22px}
.checks{left:100px;top:1846px;width:380px;list-style:none;font-size:12.5px}
.checks li{display:flex;align-items:center;gap:12px;height:31px}
.news-item{left:521px;width:580px;height:137px;border-bottom:1px solid var(--line)}
.news-thumb{position:absolute;left:2px;top:0;width:112px;height:91px}
.news-title{position:absolute;left:141px;top:0;font-family:"Open Sans",Arial,sans-serif;font-weight:600;font-size:14.5px;color:var(--ink)}
.news-date{position:absolute;left:141px;top:26px;font-size:12.5px;color:var(--teal);display:flex;align-items:center;gap:10px}
.news-text{position:absolute;left:141px;top:55px;width:440px;font-size:12.5px;line-height:22px}

/* gallery */
.filters{left:0;top:2134px;width:1200px;display:flex;justify-content:center;gap:60px;font-family:"Arimo",Arial,sans-serif;font-size:13px;color:#a8a8a8}
.filters .active{color:var(--orange);font-weight:700}
.gallery-item{top:2188px;width:229px;height:192px}
.overlay{background:var(--orange);color:var(--white);text-align:center;font-size:12.5px;line-height:21px;padding-top:48px}
.overlay .icons{display:flex;justify-content:center;gap:10px;margin-top:16px}

/* footer */
.footer{left:0;top:2442px;width:1200px;height:302px;background:var(--footer);color:var(--footer-text)}
.footer h5{font-family:"Arimo",Arial,sans-serif;font-weight:700;font-size:17px;color:var(--white)}
.footer-links{list-style:none;font-size:12.5px;line-height:25px;margin-top:12px}
.footer p{font-size:12.5px;line-height:22px}
.email-box{width:262px;height:33px;background:var(--white);color:#888;font-size:12px;padding:8px 14px;margin-top:12px}
.subscribe{width:101px;height:35px;border:2px solid var(--white);border-radius:3px;color:var(--white);font-family:"Arimo",Arial,sans-serif;font-weight:700;font-size:13px;display:flex;align-items:center;justify-content:center;margin-top:14px}
.contact-row{display:flex;gap:18px;font-size:12.5px;line-height:20px}
.social{display:flex;gap:9px}
.social span{width:34px;height:34px;border-radius:50%;border:2px solid var(--white)}
</style>
</head>
<body>

<!-- header -->
<div class="abs top-bar"></div>
<header class="abs header">
  <div class="abs brand" style="top:19px">
    <div class="brand-dot"></div>
    <div>
      <div class="brand-name">QUENBRICK HALL</div>
      <div class="brand-tag">Construction / Remodeling</div>
    </div>
  </div>
  <nav class="abs nav">
    <span class="active">HOME</span><span>ABOUT US</span><span>OUR PROJETCS</span><span>GALLERY</span><span>CONTACT US</span>
    <svg width="15" height="15" viewBox="0 0 15 15"><circle cx="6" cy="6" r="4.5" fill="none" stroke="#2b2b2b" stroke-width="2"/><line x1="9.5" y1="9.5" x2="14" y2="14" stroke="#2b2b2b" stroke-width="2.2"/></svg>
  </nav>
</header>
<div class="abs phone-tab">
  <svg width="26" height="26" viewBox="0 0 26 26"><circle cx="13" cy="13" r="11.5" fill="none" stroke="#fff" stroke-width="2"/><path d="M9 7.5l2.2 2.6-1.3 1.6c.8 1.8 2.2 3.2 4 4l1.6-1.3 2.6 2.2-1.4 1.8c-4.4-.6-8.3-4.5-8.9-8.9z" fill="#fff"/></svg>
  415.555.0142
</div>

<!-- hero -->
<section class="abs hero" role="img" aria-label="Photo of a large two-storey craftsman house with double garage, stone porch and green lawn"></section>
<h1 class="abs heading hero-title center">High End Construction / Remodeling</h1>
<p class="abs hero-sub center">At vero eos et accusamus et iusto odio dignissimos ducimus qui blanditiis praesentium voluptatum deleniti atque corrupti quos dolores et quas molestias excep</p>
<div class="abs hero-btn">VIEW OUR PROJECTS &gt;&gt;</div>
<div class="abs dots"><span></span><span></span><span></span></div>

<!-- welcome -->
<h2 class="abs heading section-title center" style="top:598px">Welcome to Quenbrick Hall</h2>
<p class="abs welcome-text center">At vero eos et accusamus et iusto odio dignissimos ducimus qui blanditiis praesentium voluptatum deleniti atque corrupti quos dolores et quas mole stias excepturi sint occaecati cupiditate non provident, similique sunt in culpa qui officia deserunt mollitia animi, id est</p>

<div class="abs feature" style="left:88px">
  <div class="feature-icon" style="background:var(--teal)" role="img" aria-label="Icon of a builder presenting a house plan"><div class="ring"></div></div>
  <h3>Remodelling</h3>
  <p>Nam libero tempore, cum soluta nobis est eligendi optio cumque nihil impedit quo minus id quod maxime placeat facere</p>
  <span class="read-more">Read more &gt;&gt;</span>
</div>
<div class="abs feature" style="left:448px">
  <div class="feature-icon" style="background:var(--orange)" role="img" aria-label="Icon of a designer presenting a house plan"><div class="ring"></div></div>
  <h3>Excellent Design</h3>
  <p>Nam libero tempore, cum soluta nobis est eligendi optio cumque nihil impedit quo minus id quod maxime placeat facere</p>
  <span class="read-more">Read more &gt;&gt;</span>
</div>
<div class="abs feature" style="left:810px">
  <div class="feature-icon" style="background:var(--teal)" role="img" aria-label="Icon of a quality award rosette"><div class="ring"></div></div>
  <h3>High Quality</h3>
  <p>Nam libero tempore, cum soluta nobis est eligendi optio cumque nihil impedit quo minus id quod maxime placeat facere</p>
  <span class="read-more">Read more &gt;&gt;</span>
</div>

<!-- recent projects -->
<section class="abs band" style="top:1043px;height:417px"></section>
<h2 class="abs heading section-title center" style="top:1080px">Recent Projects</h2>
<div class="abs arrow-btn" style="left:51px;top:1200px"><svg width="37" height="53" viewBox="0 0 37 53"><path d="M21 20l-6 6.5 6 6.5" fill="none" stroke="#999" stroke-width="2"/></svg></div>
<div class="abs arrow-btn" style="left:1109px;top:1200px"><svg width="37" height="53" viewBox="0 0 37 53"><path d="M16 20l6 6.5-6 6.5" fill="none" stroke="#999" stroke-width="2"/></svg></div>

<div class="abs project" style="left:100px">
  <div class="photo" style="height:173px;background:linear-gradient(160deg,#c9c6bf,#6c6a66 60%,#3c3b3a)" role="img" aria-label="Photo of a remodelled white kitchen with island and bar stools"></div>
  <h4>FINIBUS BONORUM ET MALO</h4>
  <p>Nam libero tempore, cum soluta nobis est eligendi optio cumque..</p>
  <span class="read-more">Read more &gt;&gt;</span>
</div>
<div class="abs project" style="left:354px">
  <div class="photo" style="height:173px;background:linear-gradient(160deg,#d8d3ca,#6b4a33 60%,#3a2a20)" role="img" aria-label="Photo of a kitchen with dark wood cabinets and pendant lights"></div>
  <h4>FINIBUS BONORUM ET MALO</h4>
  <p>Nam libero tempore, cum soluta nobis est eligendi optio cumque..</p>
  <span class="read-more">Read more &gt;&gt;</span>
</div>
<div class="abs project" style="left:608px">
  <div class="photo" style="height:173px;background:linear-gradient(180deg,#e4dccd,#b9ad98 70%,#8d8272)" role="img" aria-label="Photo of a room with a vaulted white ceiling and windows"></div>
  <h4>FINIBUS BONORUM ET MALO</h4>
  <p>Nam libero tempore, cum soluta nobis est eligendi optio cumque..</p>
  <span class="read-more">Read more &gt;&gt;</span>
</div>
<div class="abs project" style="left:862px">
  <div class="photo" style="height:173px;background:linear-gradient(160deg,#9a8f82,#cfc9bf 50%,#6e665e)" role="img" aria-label="Photo of a marble bathroom with a soaking tub"></div>
  <h4>FINIBUS BONORUM ET MALO</h4>
  <p>Nam libero tempore, cum soluta nobis est eligendi optio cumque..</p>
  <span class="read-more">Read more &gt;&gt;</span>
</div>

<!-- why choose us -->
<h2 class="abs heading" style="left:100px;top:1508px;font-size:24px">Why Choose Us</h2>
<div class="abs photo" style="left:100px;top:1564px;width:372px;height:210px;background:linear-gradient(180deg,#c9ccca,#e8ebea 45%,#5a3b2a 85%)" role="img" aria-label="Photo of an empty living room with glass patio doors and dark wood floor"></div>
<p class="abs why-text">Lorem ipsum dolor sit amet, consectetur adipiscing elit, sed do eiu smod tempor incididunt ut labore et dolore..</p>
<ul class="abs checks">
  <li><svg width="14" height="14" viewBox="0 0 14 14"><circle cx="7" cy="7" r="7" fill="#2a9fbd"/><path d="M3.8 7.2l2.2 2.1 4.2-4.3" fill="none" stroke="#fff" stroke-width="1.8"/></svg>Psam voluptatem quia voluptas sit aspernatur aut odit</li>
  <li><svg width="14" height="14" viewBox="0 0 14 14"><circle cx="7" cy="7" r="7" fill="#2a9fbd"/><path d="M3.8 7.2l2.2 2.1 4.2-4.3" fill="none" stroke="#fff" stroke-width="1.8"/></svg>Aut fugit, sed quia consequuntur magni dolores eos</li>
  <li><svg width="14" height="14" viewBox="0 0 14 14"><circle cx="7" cy="7" r="7" fill="#2a9fbd"/><path d="M3.8 7.2l2.2 2.1 4.2-4.3" fill="none" stroke="#fff" stroke-width="1.8"/></svg>Sed quia non numquam eius modi tempora incidu</li>
  <li><svg width="14" height="14" viewBox="0 0 14 14"><circle cx="7" cy="7" r="7" fill="#2a9fbd"/><path d="M3.8 7.2l2.2 2.1 4.2-4.3" fill="none" stroke="#fff" stroke-width="1.8"/></svg>Unisi ut aliquid ex ea commodi consequatur? Quis</li>
</ul>
<span class="abs read-more" style="left:96px;top:1978px">Read more &gt;&gt;</span>

<!-- news -->
<h2 class="abs heading" style="left:521px;top:1508px;font-size:24px">Our News</h2>
<div class="abs news-item" style="top:1564px">
  <div class="news-thumb photo" style="background:linear-gradient(160deg,#8a7a68,#4a3e33)" role="img" aria-label="Photo of a living room with fireplace"></div>
  <div class="news-title">AT VERO EOS ET ACCUSAMUS ET IUSTO ODIO DIG</div>
  <div class="news-date"><svg width="13" height="13" viewBox="0 0 13 13"><rect x="1" y="2" width="11" height="10" fill="none" stroke="#2a9fbd" stroke-width="1.5"/><line x1="1" y1="5" x2="12" y2="5" stroke="#2a9fbd" stroke-width="1.5"/></svg>05/03/2016</div>
  <p class="news-text">Nemo enim ipsam voluptatem quia voluptas sit aspernatur aut odit aut fugit, sed quia consequuntur..</p>
</div>
<div class="abs news-item" style="top:1701px">
  <div class="news-thumb photo" style="background:linear-gradient(180deg,#9aa3a8,#6b6a5e 55%,#3d4a2c)" role="img" aria-label="Photo of a house exterior among trees"></div>
  <div class="news-title">AT VERO EOS ET ACCUSAMUS ET IUSTO ODIO DIG</div>
  <div class="news-date"><svg width="13" height="13" viewBox="0 0 13 13"><rect x="1" y="2" width="11" height="10" fill="none" stroke="#2a9fbd" stroke-width="1.5"/><line x1="1" y1="5" x2="12" y2="5" stroke="#2a9fbd" stroke-width="1.5"/></svg>05/03/2016</div>
  <p class="news-text">Nemo enim ipsam voluptatem quia voluptas sit aspernatur aut odit aut fugit, sed quia consequuntur..</p>
</div>
<div class="abs news-item" style="top:1838px">
  <div class="news-thumb photo" style="background:linear-gradient(160deg,#d9d6d0,#8f8c86)" role="img" aria-label="Photo of a bathroom under renovation"></div>
  <div class="news-title">AT VERO EOS ET ACCUSAMUS ET IUSTO ODIO DIG</div>
  <div class="news-date"><svg width="13" height="13" viewBox="0 0 13 13"><rect x="1" y="2" width="11" height="10" fill="none" stroke="#2a9fbd" stroke-width="1.5"/><line x1="1" y1="5" x2="12" y2="5" stroke="#2a9fbd" stroke-width="1.5"/></svg>05/03/2016</div>
  <p class="news-text">Nemo enim ipsam voluptatem quia voluptas sit aspernatur aut odit aut fugit, sed quia consequuntur..</p>
</div>
<span class="abs read-more" style="left:525px;top:1978px">View more &gt;&gt;</span>

<!-- gallery -->
<section class="abs band" style="top:2040px;height:402px"></section>
<h2 class="abs heading section-title center" style="top:2086px">Our Gallery</h2>
<div class="abs filters"><span class="active">ALL</span><span>RESIDENTIAL</span><span>COMMERCIAL</span></div>
<div class="abs arrow-btn" style="left:51px;top:2258px"><svg width="37" height="53" viewBox="0 0 37 53"><path d="M21 20l-6 6.5 6 6.5" fill="none" stroke="#999" stroke-width="2"/></svg></div>
<div class="abs arrow-btn" style="left:1109px;top:2258px"><svg width="37" height="53" viewBox="0 0 37 53"><path d="M16 20l6 6.5-6 6.5" fill="none" stroke="#999" stroke-width="2"/></svg></div>

<div class="abs gallery-item photo overlay" style="left:100px">
  Lorem ipsum dolor sit amet<br>consectetur adipiscin
  <div class="icons">
    <svg width="36" height="36" viewBox="0 0 36 36"><circle cx="18" cy="18" r="16" fill="none" stroke="#fff" stroke-width="2"/><rect x="11" y="15" width="9" height="6" rx="3" fill="none" stroke="#fff" stroke-width="2" transform="rotate(-45 15.5 18)"/><rect x="16" y="15" width="9" height="6" rx="3" fill="none" stroke="#fff" stroke-width="2" transform="rotate(-45 20.5 18)"/></svg>
    <svg width="36" height="36" viewBox="0 0 36 36"><circle cx="18" cy="18" r="16" fill="none" stroke="#fff" stroke-width="2"/><circle cx="16.5" cy="16.5" r="5.5" fill="none" stroke="#fff" stroke-width="2"/><line x1="20.5" y1="20.5" x2="25" y2="25" stroke="#fff" stroke-width="2.4"/></svg>
  </div>
</div>
<div class="abs gallery-item photo" style="left:358px;background:linear-gradient(180deg,#e6e8e8,#b9c7cc 50%,#5e8ea0 60%,#e2e4e4)" role="img" aria-label="Photo of a tiled shower with a blue mosaic band"></div>
<div class="abs gallery-item photo" style="left:614px;background:linear-gradient(160deg,#b89c7a,#d8cdb9 50%,#5a4634)" role="img" aria-label="Photo of a sunlit room with armchair and wooden ceiling"></div>
<div class="abs gallery-item photo" style="left:870px;background:linear-gradient(180deg,#9aa9b3,#6a5848 55%,#b8b3aa)" role="img" aria-label="Photo of a kitchen with granite island and bay windows"></div>

<!-- footer -->
<footer class="abs footer">
  <div class="abs brand" style="top:106px">
    <div class="brand-dot" style="background:var(--white)"></div>
    <div>
      <div class="brand-name" style="color:var(--white)">QUENBRICK HALL</div>
      <div class="brand-tag" style="color:var(--white)">Construction / Remodeling</div>
    </div>
  </div>
  <div class="abs" style="left:411px;top:0;width:1px;height:230px;background:#3a3a3a"></div>

  <div class="abs" style="left:443px;top:30px">
    <h5>Information</h5>
    <ul class="footer-links"><li>Home</li><li>About us</li><li>Projects</li><li>Gallery</li><li>Contact Us</li></ul>
  </div>

  <div class="abs" style="left:596px;top:30px;width:280px">
    <h5>Newsletter</h5>
    <p style="margin-top:12px">Register your email address to get information ablout us</p>
    <div class="email-box">Email Address</div>
    <div class="subscribe">SUBSCRIBE</div>
  </div>

  <div class="abs" style="left:911px;top:30px;width:200px">
    <h5>Contact Us</h5>
    <div class="contact-row" style="margin-top:20px">
      <svg width="12" height="16" viewBox="0 0 12 16"><path d="M6 0a6 6 0 0 1 6 6c0 4-6 10-6 10S0 10 0 6a6 6 0 0 1 6-6z" fill="#fff"/><circle cx="6" cy="6" r="2.2" fill="#2a2a2a"/></svg>
      <span>1200 Alder Court, Suite 20,<br>CA 94025 Menlo Park</span>
    </div>
    <div class="contact-row" style="margin-top:22px;align-items:center">
      <svg width="13" height="13" viewBox="0 0 13 13"><path d="M1 1.5l3 0 1.2 3-1.6 1.2c.9 1.7 2 2.8 3.7 3.7L8.5 7.8l3 1.2v3c-6 .4-10.9-4.5-10.5-10.5z" fill="#fff"/></svg>
      <span>650.555.0187</span>
    </div>
    <div class="contact-row" style="margin-top:22px;align-items:center">
      <svg width="14" height="11" viewBox="0 0 14 11"><rect width="14" height="11" fill="#fff"/><path d="M0 0l7 6 7-6" fill="none" stroke="#2a2a2a" stroke-width="1.4"/></svg>
      <span>hello@quenbrickhall.com</span>
    </div>
  </div>

  <p class="abs" style="left:100px;top:254px;font-size:12px">Copyrights © 2016, Quenbrick Hall. All rights reserved.</p>
  <div class="abs social" style="left:949px;top:248px" aria-label="Social media links"><span></span><span></span><span></span><span></span></div>
</footer>

</body>
</html>
```